" Soluçoes de tecnologia focadas em impressao e outsourcing de impressao visando a reduçao de custos de impressao e a melhoria de processos para pequenas, médias e grandes empresas corporativas e governo através de licitações. Atendimento ao público(balcão) com soluções de grafica rápida, impressão de dados variáveis, impressão de provas de consursos Gerenciar e racionalizar os processos de impressao/cópia através de uso inteligente de tecnologia de última geraçao. Contabilizar páginas/cópias impressas, gerenciar suprimentos. Otimizar processos internos para cada departamento e necessidade. Solução de digitalização de documentos. "

```html
<!DOCTYPE html>
<html lang="pt-BR">
<head>
<meta charset="UTF-8">
<title>Lumi Solution — Soluções que impressionam</title>
<link href="https://fonts.googleapis.com/css2?family=Exo+2:ital,wght@1,500;1,600&family=Open+Sans:wght@400;600&display=swap" rel="stylesheet">
<style>
  :root {
    --canvas-bg: #e9e9ea;
    --nav-bg: #ffffff;
    --ink: #1a1a1a;
    --accent: #e3322d;
    --accent-soft: rgba(227, 50, 45, 0.92);
    --hero-dark: #0d0d0e;
    --hero-mid: #232325;
    --text-light: #f2f2f2;
  }
  * { margin: 0; padding: 0; box-sizing: border-box; }
  html, body {
    width: 1200px; height: 1200px; overflow: hidden;
    background: var(--canvas-bg);
  }
  .site {
    position: absolute; left: 40px; top: 268px;
    width: 1120px; height: 665px;
    overflow: hidden;
    box-shadow: 0 10px 30px rgba(0,0,0,0.18);
  }
  .site-header {
    position: absolute; left: 0; top: 0; width: 100%; height: 100px;
    background: var(--nav-bg);
    display: flex; align-items: center; justify-content: space-between;
    padding: 0 68px 0 110px;
    z-index: 3;
  }
  .brand {
    display: flex; align-items: center; gap: 12px;
    font-family: "Open Sans", sans-serif; font-weight: 600;
    font-size: 34px; color: var(--ink); letter-spacing: -0.5px;
  }
  .brand-mark { width: 26px; height: 26px; background: var(--accent); }
  .main-nav { display: flex; gap: 22px; }
  .main-nav a {
    font-family: "Open Sans", sans-serif; font-weight: 600;
    font-size: 22px; color: var(--ink); text-decoration: none;
  }
  .main-nav a.is-active { color: var(--accent); }

  .hero {
    position: absolute; left: 0; top: 100px; width: 100%; height: 565px;
    background: radial-gradient(ellipse at 30% 45%, var(--hero-mid) 0%, var(--hero-dark) 70%);
  }
  .hero-squares { position: absolute; inset: 0; z-index: 1; }
  .hero-photo {
    position: absolute; left: 660px; top: 215px; width: 460px; height: 350px;
    background: linear-gradient(160deg, #f4f4f5 0%, #c9cacc 45%, #6c6e72 80%, #2a2b2d 100%);
    border-radius: 6px 0 0 0;
    z-index: 2;
  }
  .hero-title {
    position: absolute; left: 70px; top: 60px; z-index: 2;
    font-family: "Exo 2", sans-serif; font-style: italic;
    color: var(--text-light); text-transform: uppercase; line-height: 1.1;
  }
  .hero-title .line-small { display: block; font-size: 40px; font-weight: 500; letter-spacing: 4px; }
  .hero-title .line-large { display: block; font-size: 54px; font-weight: 600; letter-spacing: 3px; }
  .hero-text {
    position: absolute; left: 30px; top: 200px; width: 600px; z-index: 2;
    font-family: "Open Sans", sans-serif; font-size: 21px; line-height: 40px;
    color: var(--text-light); text-align: center;
  }
  .hero-text span { display: block; white-space: nowrap; }
</style>
</head>
<body>
  <main class="site">
    <header class="site-header">
      <div class="brand"><span class="brand-mark"></span>lumi solution</div>
      <nav class="main-nav">
        <a href="#">Home</a>
        <a href="#" class="is-active">Quem Somos</a>
        <a href="#">Serviços</a>
        <a href="#">Fale Conosco</a>
      </nav>
    </header>

    <section class="hero">
      <svg class="hero-squares" width="1120" height="565" viewBox="0 0 1120 565">
        <rect x="860" y="0" width="150" height="140" fill="var(--accent-soft)"/>
        <rect x="725" y="140" width="135" height="125" fill="var(--accent-soft)"/>
        <rect x="1010" y="170" width="80" height="85" fill="var(--accent-soft)"/>
      </svg>
      <h1 class="hero-title">
        <span class="line-small">Soluções que</span>
        <span class="line-large">Impressionam</span>
      </h1>
      <p class="hero-text">
        <span>Soluções de tecnologia focadas</span>
        <span>em impressão e outsourcing de impressão</span>
        <span>visando a redução de custos de impressão e a</span>
        <span>melhoria de processos para pequenas, médias e</span>
        <span>grandes empresas corporativas e governo</span>
        <span>através de licitações.</span>
      </p>
      <div class="hero-photo" role="img" aria-label="Fotografia de uma impressora multifuncional corporativa branca e cinza"></div>
    </section>
  </main>
</body>
</html>
```